Groovy little Insurance brokerage needs a new look

We have a new logo, but need to work out how to make it work for us!
We are a small insurance broking firm (three staff with different focus and styles), with lots of energy, experience and enthusiasm. A focus on both commercial and domestic market. We would like our cards to show a fresh look - while veering away from the 'run of the mill' insurance industry (often dull) approach.
Updates

Thanks to all for your concepts.

Had some great ideas come back, now just the process of picking which one is going to work best for us...
Will advise when we've had an opportunity to review.

Thanks!
From the team at
Quarry Tidewell Insurance Brokers

Thanks SO much to all of your for your great designs.  Now just a process of sorting out the favorites.  If yours is eliminated, just want to say a collective thank you for your efforts!

Industry/Entity Type

Business

```html
<!DOCTYPE html>
<html lang="en">
<head>
<meta charset="utf-8">
<title>Quarry Tidewell Insurance Brokers — Business Card</title>
<link rel="stylesheet" href="https://fonts.googleapis.com/css2?family=Poppins:wght@500;600&display=swap">
<style>
  :root {
    --teal: #20afc6;
    --ink: #333132;
    --paper: #ffffff;
    --edge: #3a3a3a;
  }
  html, body {
    margin: 0;
    padding: 0;
    width: 1200px;
    height: 668px;
    overflow: hidden;
    background: var(--paper);
  }
  .card {
    position: relative;
    width: 1200px;
    height: 668px;
    box-sizing: border-box;
    border: 2px solid var(--edge);
    background: var(--paper);
    overflow: hidden;
    font-family: "Poppins", sans-serif;
    font-weight: 500;
    color: var(--ink);
  }
  .card__wave {
    position: absolute;
    inset: 0;
    width: 100%;
    height: 100%;
  }
  .card__wave path { fill: var(--teal); }

  .person {
    position: absolute;
    left: 103px;
    top: 92px;
    margin: 0;
    font-size: 26px;
    line-height: 34px;
    letter-spacing: 3px;
  }
  .person__name { display: block; color: var(--teal); }
  .person__role { display: block; color: var(--ink); }

  .contact {
    position: absolute;
    left: 103px;
    top: 288px;
    margin: 0;
    padding: 0;
    list-style: none;
    font-size: 26px;
    line-height: 37.5px;
    letter-spacing: 2.5px;
  }
  .contact__label { color: var(--teal); }

  .address {
    position: absolute;
    left: 103px;
    top: 514px;
    margin: 0;
    font-style: normal;
    font-size: 26px;
    line-height: 34px;
    letter-spacing: 2.5px;
  }

  .brand {
    position: absolute;
    left: 607px;
    top: 82px;
    display: flex;
    align-items: center;
    gap: 16px;
  }
  .brand__square {
    width: 127px;
    height: 134px;
    background: var(--teal);
    flex: none;
  }
  .brand__text { display: flex; flex-direction: column; }
  .brand__name {
    font-size: 43px;
    line-height: 1;
    font-weight: 600;
    color: var(--ink);
    white-space: nowrap;
    letter-spacing: 0.5px;
  }
  .brand__tagline {
    margin-top: 14px;
    font-size: 13.5px;
    font-weight: 600;
    color: var(--teal);
    letter-spacing: 0.6px;
    white-space: nowrap;
  }
</style>
</head>
<body>
  <main class="card">
    <svg class="card__wave" viewBox="0 0 1200 668" aria-hidden="true">
      <path d="M501,668 C545,560 650,480 830,445 C1000,412 1130,330 1200,240 L1200,668 Z"/>
    </svg>

    <p class="person">
      <span class="person__name">Dalen</span>
      <span class="person__role">C.E.O</span>
    </p>

    <ul class="contact">
      <li><span class="contact__label">T:</span> +00 0000 0000</li>
      <li><span class="contact__label">M:</span>+00 0000 0000</li>
      <li><span class="contact__label">E:</span>abc@abc.com</li>
    </ul>

    <address class="address">
      #123, Street name,<br>
      City name - 000000
    </address>

    <div class="brand">
      <div class="brand__square"></div>
      <div class="brand__text">
        <span class="brand__name">Quarry Tidewell</span>
        <span class="brand__tagline">QUARRY TIDEWELL INSURANCE BROKERS</span>
      </div>
    </div>
  </main>
</body>
</html>
```